Bold & Power Webpage for VANTA Medical a Novel Business Solution for Clinical Labs

Informative and interactive webpage that utilizes my logo and information to draw customers into our company. The consulting company has 5 major functions.
1. Scientific Support to Clinical Sales
2. Clinical Lab Consulting
3. Develops Novel Diagnostic Test for Clinical labs
4. Process Optimization for Business
5. Physician Support for clinical results

The page should be dynamic and attractive from a marketing perspective. It should access points to upload new information in the form of publications, papers and videos. The website should have a means to be educational as well with a dynamic presentation of the information.

Target Market(s)

Medical Sales Reps
Clinical Laboratories
Medical Professionals
Scientist

Coding

Number of Pages Required

Font styles to use
Serif

Requirements
Must have
• Bold Colors, Dynamic presentation, fluid transitions, ability to request info, add PDF type information, Must professional and visually impressive
Nice to have
• Ability to upload videos, request information

```html
<!DOCTYPE html>
<html lang="en">
<head>
<meta charset="utf-8">
<title>VANTA Medical – Brightline Advisory</title>
<link href="https://fonts.googleapis.com/css2?family=Roboto:wght@300;400;500;700&family=Nothing+You+Could+Do&display=swap" rel="stylesheet">
<style>
:root{
  --navy:#0f4a82;
  --navy-deep:#124b85;
  --blue-mid:#1f5b93;
  --blue-dark:#174c84;
  --title-blue:#174f8a;
  --nav-bg:#eaeef2;
  --section-bg:#e9edf1;
  --light-bg:#f3f6f9;
  --green:#4cb81f;
  --badge-bg:#ffffff;
  --badge-line:#c9d5e2;
  --text:#3d4650;
  --muted:#7b8590;
  --white:#ffffff;
}
*{box-sizing:border-box;margin:0;padding:0}
html,body{width:1200px;height:2284px;overflow:hidden}
body{font-family:"Roboto",Arial,sans-serif;color:var(--text);background:var(--white)}
a{color:inherit;text-decoration:none}

.topbar{height:34px;background:var(--navy);color:#fff;font-size:14px;display:flex;align-items:center;padding:0 52px}
.topbar .item{display:flex;align-items:center;gap:8px;margin-right:24px}
.topbar .right{margin-left:auto;display:flex;align-items:center;gap:20px}
.dot-icon{width:10px;height:10px;border-radius:50%;background:#fff;display:inline-block}

.nav{height:68px;background:var(--nav-bg);display:flex;align-items:center;padding:0 52px}
.brand{display:flex;align-items:center;gap:12px;font-size:30px;font-weight:400;color:var(--title-blue)}
.brand-mark{width:40px;height:40px;border-radius:50%;background:#2d7fcf}
.menu{margin-left:auto;display:flex;gap:38px;font-size:15px;font-weight:500;color:var(--navy)}

.hero{position:relative;height:489px;background:
  radial-gradient(circle at 86% 28%,#fffbe0 0,#ffe95a 8%,rgba(255,220,40,0) 30%),
  linear-gradient(180deg,#d7a317 0%,#f0c928 22%,#e1c11c 42%,#a9a415 62%,#8a9312 80%,#6f8410 100%);
  text-align:center;color:#fff}
.hero h1{font-family:"Nothing You Could Do",cursive;font-weight:400;font-size:66px;line-height:72px;padding-top:66px;text-shadow:0 2px 6px rgba(0,0,0,.25)}
.hero p{font-size:20px;line-height:30px;margin:16px auto 0;width:540px;font-weight:500;text-shadow:0 1px 3px rgba(0,0,0,.3)}
.hero-actions{margin-top:26px;display:flex;justify-content:center;gap:50px}
.btn-solid,.btn-ghost{display:inline-block;height:31px;line-height:31px;padding:0 14px;font-size:10px;font-weight:700;border-radius:3px}
.btn-solid{background:#fff;color:var(--navy)}
.btn-ghost{border:1px solid #fff;color:#fff;padding:0 13px;line-height:29px}
.hero-dots{position:absolute;left:0;right:0;bottom:20px;display:flex;justify-content:center;gap:10px}
.hero-dots span{width:10px;height:10px;border-radius:50%;background:#fff}
.hero-dots span.off{background:transparent;border:1.5px solid #fff}

.intro{height:221px;background:var(--light-bg);text-align:center;padding-top:10px}
.section-title{font-size:22px;font-weight:700;color:var(--title-blue)}
.rule{border-top:1.5px dotted var(--title-blue);margin:12px 52px 0}
.intro p{font-size:12px;line-height:20px;margin-top:54px;padding:0 40px}
.tag{display:inline-block;margin-top:8px;background:var(--green);color:#fff;font-size:14px;font-weight:700;padding:6px 12px;border-radius:3px}

.band{height:271px;background:radial-gradient(ellipse at 50% 62%,#6c86c8 0,#3f5ca6 16%,#1e3f7a 32%,rgba(40,80,140,.6) 48%,transparent 62%),linear-gradient(90deg,#0c2340 0%,#2a5a90 30%,#7fb2dc 62%,#cfe6f5 82%,#a8cdec 100%)}

.services{position:relative;height:407px;background:var(--section-bg);padding-top:16px;text-align:center}
.service{position:absolute;top:98px;width:200px}
.service.s1{left:42px}.service.s2{left:252px}.service.s3{left:474px;width:240px}.service.s4{left:736px}.service.s5{left:942px}
.badge{width:122px;height:122px;border-radius:50%;background:var(--badge-bg);border:3px solid var(--badge-line);margin:0 auto;display:flex;align-items:center;justify-content:center}
.service h3{font-size:19px;line-height:24px;font-weight:700;color:#2b2f33;margin-top:10px}
.service p{font-size:13px;line-height:18px;color:var(--muted);margin-top:16px;font-weight:300;padding:0 8px}

.faq{height:423px;display:flex}
.faq-col{flex:1;background:var(--blue-mid);color:#fff;padding:38px 48px 0;position:relative}
.faq-col.alt{background:var(--blue-dark)}
.faq-col h4{font-size:18px;line-height:24px;font-weight:500}
.faq-col p{font-size:14px;line-height:22px;margin-top:26px;font-weight:300;padding-right:30px}
.faq-col .btn-line{position:absolute;left:48px;top:369px;border:1px solid #fff;border-radius:3px;font-size:13px;font-weight:500;height:37px;line-height:35px;padding:0 18px}

.likebar{height:72px;background:var(--light-bg);display:flex;justify-content:center;align-items:center}
.like-pill{width:448px;height:45px;background:#fff;border-radius:23px;display:flex;align-items:center;font-size:11px;color:#333}
.like-pill .thumb{width:58px;height:100%;border-right:1px solid #e3e6ea;display:flex;align-items:center;justify-content:center}
.like-pill .thumb span{width:14px;height:14px;border-radius:3px;background:#c7ccd3}
.like-btn{background:#4267b2;color:#fff;font-weight:700;font-size:10px;padding:3px 6px;border-radius:2px;margin:0 6px 0 62px}

.footer{height:299px;background:var(--navy-deep);color:#fff;padding:38px 52px 0;position:relative}
.footer-cols{display:flex}
.footer-col{width:282px}
.footer-col h5{font-size:18px;font-weight:500}
.footer-col p{font-size:12.5px;line-height:20px;color:#a7bdd6;margin-top:14px;font-weight:300}
.footer-col p + p.line{margin-top:13px}
.footer-col .lbl{color:#cfdceb}
.footer-social{width:10px;height:10px;border-radius:50%;background:#a7bdd6;margin-top:18px}
.footer-bottom{position:absolute;left:52px;right:52px;top:236px;border-top:1px solid #2a5e96;text-align:center;padding-top:20px;font-size:12px;color:#a7bdd6}
</style>
</head>
<body>

<header>
  <div class="topbar">
    <span class="item"><svg width="12" height="12" viewBox="0 0 24 24"><path fill="#fff" d="M6.6 10.8a15.1 15.1 0 0 0 6.6 6.6l2.2-2.2c.3-.3.7-.4 1-.2 1.1.4 2.3.6 3.6.6.6 0 1 .4 1 1V20c0 .6-.4 1-1 1A17 17 0 0 1 3 4c0-.6.4-1 1-1h3.5c.6 0 1 .4 1 1 0 1.3.2 2.5.6 3.6.1.3 0 .7-.2 1z"/></svg>(555)010-4827</span>
    <span class="item"><svg width="14" height="11" viewBox="0 0 14 11"><rect x="0.5" y="0.5" width="13" height="10" fill="#fff"/><path d="M1 1l6 5 6-5" stroke="#0f4a82" fill="none"/></svg>mhale@brightline-advisory.net</span>
    <div class="right">
      <span class="dot-icon"></span>
      <span class="dot-icon"></span>
      <span class="item" style="margin:0"><svg width="12" height="12" viewBox="0 0 12 12"><path d="M1 6h7M5 3l3 3-3 3M8 1h3v10H8" stroke="#fff" stroke-width="1.5" fill="none"/></svg>Login</span>
      <svg width="14" height="14" viewBox="0 0 14 14"><circle cx="6" cy="6" r="4.5" stroke="#fff" stroke-width="2" fill="none"/><path d="M9.5 9.5L13 13" stroke="#fff" stroke-width="2"/></svg>
    </div>
  </div>
  <nav class="nav">
    <a class="brand" href="#"><span class="brand-mark"></span>VANTA Medical</a>
    <div class="menu">
      <a href="#">COMPANY</a><a href="#">SERVICES</a><a href="#">STAFF</a><a href="#">ANNOUNCEMENTS</a><a href="#">CAREERS</a><a href="#">CONTACT</a>
    </div>
  </nav>
</header>

<section class="hero" role="img" aria-label="Wheat field in golden sunlight">
  <h1>Welcome to<br>Brightline Advisory</h1>
  <p>Brightline Advisory is a consulting firm that specializes clinical diagnostic method development. We operate nationwide.</p>
  <div class="hero-actions">
    <a class="btn-solid" href="#">ABOUT US</a>
    <a class="btn-ghost" href="#">GO ON SURFING</a>
  </div>
  <div class="hero-dots"><span></span><span class="off"></span><span></span><span></span></div>
</section>

<section class="intro">
  <h2 class="section-title">Clinical &amp; Agricultural, Petroleum, and Forensic</h2>
  <div class="rule"></div>
  <p>Brightline Advisory is a consulting firm that specializes clinical diagnostic method development. We operate nationwide.<br>
  Brightline Advisory exists to empower clinical, agricultural, petroleum, and forensic laboratories through the use of technology and equipment, so that processes can be leaned out to reduce operating<br>
  cost without compromising quality. Brightline Advisory has the technical skill and medical licensure to guide a potential client from collection to collection.</p>
  <span class="tag">MARA HALE - CHIEF SCIENTIFIC OFFICER &amp; MANAGING PARTNER</span>
</section>

<section class="band" role="img" aria-label="Microscopic view of a blue cell"></section>

<section class="services">
  <h2 class="section-title">What We Do For You</h2>
  <div class="rule"></div>
  <div class="service s1">
    <div class="badge"><svg width="56" height="56" viewBox="0 0 56 56"><rect x="6" y="34" width="10" height="16" fill="var(--navy)"/><rect x="23" y="22" width="10" height="28" fill="var(--navy)"/><rect x="40" y="10" width="10" height="40" fill="var(--navy)"/></svg></div>
    <h3>Scientific Support to Clinical Sales</h3>
    <p>Temporibus autem quibusdam et aut officiis debitis aut rerum einem.</p>
  </div>
  <div class="service s2">
    <div class="badge"><svg width="60" height="60" viewBox="0 0 60 60"><path d="M30 16L16 42M30 16L44 42M16 42H44" stroke="var(--navy)" stroke-width="5"/><circle cx="30" cy="14" r="9" fill="#fff" stroke="var(--navy)" stroke-width="5"/><circle cx="15" cy="44" r="9" fill="#fff" stroke="var(--navy)" stroke-width="5"/><circle cx="45" cy="44" r="9" fill="#fff" stroke="var(--navy)" stroke-width="5"/></svg></div>
    <h3>Clinical Lab Consulting</h3>
    <p>Temporibus autem quibusdam et aut officiis debitis aut rerum einem.</p>
  </div>
  <div class="service s3">
    <div class="badge"><svg width="56" height="56" viewBox="0 0 56 56"><circle cx="28" cy="28" r="22" fill="none" stroke="var(--navy)" stroke-width="5"/><path d="M17 29l8 8 15-17" stroke="var(--navy)" stroke-width="6" fill="none"/></svg></div>
    <h3>Develops Novel Diagnostic Test for Clinical labs</h3>
    <p>Temporibus autem quibusdam et aut officiis debitis aut rerum einem.</p>
  </div>
  <div class="service s4">
    <div class="badge"><svg width="60" height="60" viewBox="0 0 60 60"><path d="M10 26A21 21 0 0 1 46 16M50 34A21 21 0 0 1 14 44" stroke="var(--navy)" stroke-width="7" fill="none"/><path d="M42 6l10 12-14 2zM18 54L8 42l14-2z" fill="var(--navy)"/></svg></div>
    <h3>Process Optimization for Business</h3>
    <p>Temporibus autem quibusdam et aut officiis debitis aut rerum einem.</p>
  </div>
  <div class="service s5">
    <div class="badge"><svg width="50" height="50" viewBox="0 0 50 50"><path d="M18 4h14v14h14v14H32v14H18V32H4V18h14z" fill="var(--navy)"/></svg></div>
    <h3>Physician Support for Clinical Results</h3>
    <p>Temporibus autem quibusdam et aut officiis debitis aut rerum einem.</p>
  </div>
</section>

<section class="faq">
  <article class="faq-col">
    <h4>Are the Test<br>accurate?</h4>
    <p>Veridan Biomedical lab developed test undergo extensive validation, establishment testing, as well as and rigorous peer review. Results are compared to traditional clinical chemistry results, as well as external controls whenever available to insure results are accurate and reproducible every time. Patient samples are tested in a highly complex NLAB accredited laboratory.</p>
    <a class="btn-line" href="#">LEARN MORE</a>
  </article>
  <article class="faq-col alt">
    <h4>Are the Test accepted<br>by Insurance and NationCare?</h4>
    <p>All of the tests currently offered by Veridan are reimbursed by NationCare, and the clinical lab is in network with private payers which insures private payer reimbursement. Many of the tests offered by Veridan Biomedical have been a part of clinical chemistry and/or toxicology for years. The scientific advancement only reduces sample volume requirements and allows for easy collection of sample.</p>
    <a class="btn-line" href="#">LEARN MORE</a>
  </article>
  <article class="faq-col">
    <h4>How long does it take<br>to receive my results?</h4>
    <p>Results are available electronically or by fax within 72-96 hours of the sample arriving in the lab. Sample collection kits and shipping materials are provided to the office and samples are shipped via SwiftShip overnight. This means actionable results faster, so that the best care is provided to the patient. A web based requisition and reporting function reduces the turn-around time and facilitates the awesomeness of stuff?</p>
    <a class="btn-line" href="#">LEARN MORE</a>
  </article>
</section>

<section class="likebar">
  <div class="like-pill">
    <div class="thumb"><span></span></div>
    <span class="like-btn">✓ Like</span>You and 4.1k others like this.
  </div>
</section>

<footer class="footer">
  <div class="footer-cols">
    <div class="footer-col">
      <h5>Contact</h5>
      <p>Please feel free to contact us for any issue.<br>Our staff is available to you from 9AM until<br>5PM on weekdays.</p>
      <div class="footer-social"></div>
    </div>
    <div class="footer-col">
      <h5>Phone number</h5>
      <p><span class="lbl">Phone 1:</span> (555)010-4827</p>
      <p class="line"><span class="lbl">Phone 2:</span> (555)010-4827</p>
    </div>
    <div class="footer-col">
      <h5>Office</h5>
      <p><span class="lbl">Address:</span> 4200, Alder Row 12</p>
      <p class="line"><span class="lbl">City:</span> Eastbrook, Ohio</p>
    </div>
    <div class="footer-col">
      <h5>E-Mail</h5>
      <p><span class="lbl">Info:</span> info@brightline-advisory.com</p>
    </div>
  </div>
  <div class="footer-bottom">© 2001-2016 Brightline Advisory</div>
</footer>

</body>
</html>
```